You are cordially invited to attend a delicious Afternoon Tea at The Harcourt.

Enjoy a glass of sparkling wine whilst afternoon delicacies and a menu of fine teas is presented for you to enjoy throughout the afternoon.

This is an opportunity to get together with a table of like minded ladies just for fun and to share some stories and meet some new friends.

Date: 8 August 2014
Time: 12pm - 2pm
Venue: 48 Larkmoor Lane, Melbourne VIC 3000

(hello please see above text we require - we would like to invite our clients to an afternoon tea, an invitation (hard copy) to be of elegant taste, nice lettering, pic added to the invite).

```html
<!DOCTYPE html>
<html lang="en">
<head>
<meta charset="utf-8">
<title>Afternoon Tea at The Harcourt – Invitation</title>
<link rel="stylesheet" href="https://fonts.googleapis.com/css2?family=Great+Vibes&family=Cormorant+Garamond:wght@500;600&family=Fira+Sans+Condensed:wght@300;400&display=swap">
<style>
  :root {
    --paper-light: #f6f0dc;
    --paper-dark: #e8dfc3;
    --ink: #4a3c31;
    --ink-soft: #3b2f26;
    --rule: #8a7a68;
    --frame: #5b4c3f;
    --ornament: #cbbd9f;
    --photo-top: #c9a77a;
    --photo-mid: #b88f5e;
    --photo-low: #eeeae2;
  }
  * { margin: 0; padding: 0; box-sizing: border-box; }
  html, body { width: 1200px; height: 780px; overflow: hidden; }
  body { background: var(--paper-light); }
  .invitation {
    position: relative;
    width: 1200px;
    height: 780px;
    background: radial-gradient(ellipse at 50% 45%, var(--paper-light) 0%, var(--paper-light) 45%, var(--paper-dark) 100%);
    color: var(--ink);
  }
  .corner-ornament {
    position: absolute;
    width: 140px;
    height: 140px;
    background: var(--ornament);
    opacity: 0.35;
  }
  .corner-ornament.top-left { left: 15px; top: 12px; }
  .corner-ornament.top-right { right: 10px; top: 12px; }
  .corner-ornament.bottom-left { left: 15px; bottom: 10px; }
  .corner-ornament.bottom-right { right: 10px; bottom: 10px; }
  .headline {
    position: absolute;
    top: 10px;
    left: 0;
    width: 100%;
    text-align: center;
    font-family: "Great Vibes", cursive;
    font-weight: 400;
    font-size: 72px;
    line-height: 1.2;
    color: var(--ink);
  }
  .subline {
    position: absolute;
    top: 104px;
    left: 0;
    width: 100%;
    text-align: center;
    font-family: "Cormorant Garamond", serif;
    font-weight: 600;
    font-size: 36px;
    line-height: 1.2;
    color: var(--ink);
  }
  .photo-frame {
    position: absolute;
    left: 0;
    top: 0;
  }
  .details {
    position: absolute;
    top: 622px;
    left: 0;
    width: 100%;
    text-align: center;
    font-family: "Fira Sans Condensed", sans-serif;
    font-weight: 300;
    font-size: 16px;
    line-height: 36px;
    color: var(--ink-soft);
  }
  .event-facts {
    position: absolute;
    top: 702px;
    left: 405px;
    display: flex;
    height: 64px;
    font-family: "Cormorant Garamond", serif;
    color: var(--ink);
  }
  .fact {
    border-left: 1px solid var(--rule);
    display: flex;
    flex-direction: column;
    justify-content: center;
    align-items: center;
  }
  .fact:last-child { border-right: 1px solid var(--rule); }
  .fact-date { width: 126px; }
  .fact-date .day { font-size: 44px; line-height: 40px; font-weight: 500; }
  .fact-date .month { font-size: 15px; line-height: 20px; margin-top: 4px; }
  .fact-time { width: 107px; align-items: flex-start; padding-left: 22px; }
  .fact-time .slot { font-size: 32px; line-height: 30px; font-weight: 500; }
  .fact-time .slot small { font-size: 15px; margin-left: 3px; }
  .fact-venue { width: 157px; font-size: 15px; line-height: 30px; text-align: center; }
</style>
</head>
<body>
  <main class="invitation">
    <div class="corner-ornament top-left" role="img" aria-label="Engraved flourish corner ornament"></div>
    <div class="corner-ornament top-right" role="img" aria-label="Engraved flourish corner ornament"></div>
    <div class="corner-ornament bottom-left" role="img" aria-label="Engraved flourish corner ornament"></div>
    <div class="corner-ornament bottom-right" role="img" aria-label="Engraved flourish corner ornament"></div>

    <h1 class="headline">You are cordially invited</h1>
    <h2 class="subline">to attend a delicious Afternoon Tea at The Harcourt</h2>

    <svg class="photo-frame" width="1200" height="780" viewBox="0 0 1200 780">
      <defs>
        <linearGradient id="tea-room" x1="0" y1="0" x2="0" y2="1">
          <stop offset="0" stop-color="var(--photo-top)"/>
          <stop offset="0.55" stop-color="var(--photo-mid)"/>
          <stop offset="0.62" stop-color="var(--photo-low)"/>
          <stop offset="1" stop-color="var(--photo-low)"/>
        </linearGradient>
      </defs>
      <path d="M67,158 H1120 A10,10 0 0 0 1130,168 V600 A10,10 0 0 0 1120,610 H67 A10,10 0 0 0 57,600 V168 A10,10 0 0 0 67,158 Z"
            fill="none" stroke="var(--frame)" stroke-width="1.5"/>
      <path role="img" aria-label="Photograph of an elegant afternoon tea table set with a tiered stand of scones, cakes and sandwiches, sparkling wine and fine china, between two upholstered chairs and draped curtains"
            d="M70,162 H1117 A9,9 0 0 0 1126,171 V597 A9,9 0 0 0 1117,606 H70 A9,9 0 0 0 61,597 V171 A9,9 0 0 0 70,162 Z"
            fill="url(#tea-room)"/>
    </svg>

    <section class="details">
      <p>Enjoy a glass of sparkling wine whilst afternoon delicacies and a menu of fine teas is presented for you to enjoy throughout the afternoon.</p>
      <p>This is an opportunity to get together with a table of like minded ladies just for fun and to share some stories and meet some new friends.</p>
    </section>

    <section class="event-facts">
      <div class="fact fact-date">
        <span class="day">8</span>
        <span class="month">August 2014</span>
      </div>
      <div class="fact fact-time">
        <span class="slot">12<small>pm</small></span>
        <span class="slot">02<small>pm</small></span>
      </div>
      <div class="fact fact-venue">
        <span>48 Larkmoor Lane,</span>
        <span>Melbourne VIC 3000</span>
      </div>
    </section>
  </main>
</body>
</html>
```